Golden Harbor Market VIP Card(Magnetic strip plastic card)

We need Fancy,Simple,VIP customer card design for a grocery store name"Golden Harbor Market", Chinese name"金港商场“.Major color should be Dark red. This design is based on a VIP gift card project, which means design should consider about the back side with magnetic strip area and mostly it will be plastic material.

Target Market(s)

Rich Customers

Industry/Entity Type

Grocery Store

Contact Information for Business Card

People actually put more than $1000 into the card for shopping

Font styles to use
Serif
Sans Serif
Decorative
Script
Other font styles liked:
• Fancy

Colors
ec1f27
fbed22

Requirements
Must have
• Red color
Nice to have
• Better logo transformation.

```html
<!DOCTYPE html>
<html lang="en">
<head>
<meta charset="utf-8">
<title>Golden Harbor Market VIP Card</title>
<link rel="stylesheet" href="https://fonts.googleapis.com/css2?family=Questrial&family=Noto+Sans+SC:wght@300&display=swap">
<style>
  :root {
    --red-bright: #ec1f27;
    --red-dark: #b71424;
    --gold: #fbed22;
    --white: #ffffff;
    --strip: #3a393b;
    --rule: #231f20;
    --page: #ffffff;
  }
  * { margin: 0; padding: 0; box-sizing: border-box; }
  html, body { width: 1200px; height: 900px; overflow: hidden; background: var(--page); }
  .sheet { position: relative; width: 1200px; height: 900px; }

  .card {
    position: absolute;
    width: 524px; height: 276px;
    border-radius: 12px;
    overflow: hidden;
    font-family: "Questrial", sans-serif;
  }
  .card-art { position: absolute; inset: 0; width: 100%; height: 100%; display: block; }

  .front-1 { left: 61px; top: 76px; }
  .front-2 { left: 61px; top: 389px; width: 525px; }
  .back-1  { left: 614px; top: 76px; }
  .back-2  { left: 615px; top: 389px; width: 526px; }

  .vip-tag {
    position: absolute; right: 12px; top: 4px;
    color: var(--gold); font-size: 17px; letter-spacing: -0.2px;
  }
  .name-cn {
    position: absolute; left: 78px; top: 58px;
    font-family: "Noto Sans SC", sans-serif; font-weight: 300;
    color: var(--white); font-size: 93px; line-height: 1; letter-spacing: -2px;
  }
  .name-en {
    position: absolute; left: 81px; top: 168px;
    font-size: 33.5px; line-height: 1; letter-spacing: -1px;
    color: var(--gold); white-space: nowrap;
  }
  .front-2 .name-en { color: var(--white); }

  .holder {
    position: absolute; left: 19px; top: 20px;
    color: var(--white); font-size: 24px; line-height: 30px;
  }
  .monogram {
    position: absolute; right: 12px; top: 158px;
    color: var(--gold); font-size: 37px; line-height: 1; letter-spacing: -1px;
  }

  .page-rule {
    position: absolute; left: 0; top: 777px; width: 1200px; height: 2px;
    background: var(--rule);
  }
</style>
</head>
<body>
<main class="sheet">

  <section class="card front-1" aria-label="Card front, gold name">
    <svg class="card-art" viewBox="0 0 524 276" preserveAspectRatio="none" aria-hidden="true">
      <rect width="524" height="276" fill="var(--red-dark)"/>
      <polygon points="9,0 524,0 524,157 166,157" fill="var(--red-bright)"/>
      <line x1="0" y1="81" x2="80" y2="81" stroke="var(--white)" stroke-width="3"/>
      <line x1="446" y1="93" x2="524" y2="93" stroke="var(--white)" stroke-width="3"/>
    </svg>
    <p class="vip-tag">☆ VIP Member</p>
    <h1 class="name-cn">金港商场</h1>
    <p class="name-en">GOLDEN HARBOR MARKET</p>
  </section>

  <section class="card back-1" aria-label="Card back">
    <svg class="card-art" viewBox="0 0 524 276" preserveAspectRatio="none" aria-hidden="true">
      <rect width="524" height="276" fill="var(--red-bright)"/>
      <polygon points="0,0 516,0 358,157 0,157" fill="var(--red-dark)"/>
      <rect y="202" width="524" height="52" fill="var(--strip)"/>
    </svg>
    <p class="holder">Firstname Lastname<br>Card ID</p>
    <p class="monogram">GHM</p>
  </section>

  <section class="card front-2" aria-label="Card front, white name">
    <svg class="card-art" viewBox="0 0 525 276" preserveAspectRatio="none" aria-hidden="true">
      <rect width="525" height="276" fill="var(--red-dark)"/>
      <polygon points="9,0 525,0 525,157 166,157" fill="var(--red-bright)"/>
      <line x1="0" y1="81" x2="80" y2="81" stroke="var(--white)" stroke-width="3"/>
      <line x1="446" y1="93" x2="525" y2="93" stroke="var(--white)" stroke-width="3"/>
    </svg>
    <p class="vip-tag">☆ VIP Member</p>
    <h2 class="name-cn">金港商场</h2>
    <p class="name-en">GOLDEN HARBOR MARKET</p>
  </section>

  <section class="card back-2" aria-label="Card back">
    <svg class="card-art" viewBox="0 0 526 276" preserveAspectRatio="none" aria-hidden="true">
      <rect width="526" height="276" fill="var(--red-bright)"/>
      <polygon points="0,0 518,0 360,157 0,157" fill="var(--red-dark)"/>
      <rect y="203" width="526" height="52" fill="var(--strip)"/>
    </svg>
    <p class="holder">Firstname Lastname<br>Card ID</p>
    <p class="monogram">GHM</p>
  </section>

  <div class="page-rule" aria-hidden="true"></div>
</main>
</body>
</html>
```